Real Estate Website

The existing website design is http://brevanola.quillset4.com.au/ and we are not happy with it and need a fresh new design.

The menu of the website should be as it is however the content on the home page needs to include the following:

* Some sort of feature image/slideshow
* Introduction text and photo
* Our services section with boxes for 'strata management' 'property management' and 'property valuation & brokerage'. These boxes will then link to specific areas in the website
* Where are we with the contact details
* contact us with a form asking for name, email, phone, service interested in (as a dropdown) and comments box.
(do not include the who we are section)

In regards to design style/layout, here is what we like:
https://tarnelbeans.com/us/
https://www.coverlyne.com.au/
https://www.pendrake.com.au/
https://www.hqz.com/
https://www.vornelli.com.au/

```html
<!DOCTYPE html>
<html lang="en">
<head>
<meta charset="utf-8">
<title>Brevan &amp; Quill — Real Estate</title>
<link href="https://fonts.googleapis.com/css2?family=Libre+Baskerville:wght@400;700&family=Poppins:wght@300;400;500&display=swap" rel="stylesheet">
<style>
:root{
  --navy:#283687;
  --green:#12913f;
  --paper:#f4f4f4;
  --white:#ffffff;
  --ink:#222433;
  --muted:#6d6f7a;
  --sky:#8ea0ff;
  --line:#dcdde3;
}
*{box-sizing:border-box;margin:0;padding:0}
html,body{width:1200px;height:2952px;overflow:hidden}
body{position:relative;background:var(--paper);font-family:'Poppins',sans-serif;color:var(--ink)}
.abs{position:absolute}
.serif{font-family:'Libre Baskerville',serif}
.band-top{left:0;top:0;width:1200px;height:533px;background:var(--navy)}
.logo{left:100px;top:18px;color:var(--white);font-size:26px;font-weight:700}
.nav{left:433px;top:0;height:68px;display:flex;align-items:center;gap:0}
.nav a{font-family:'Libre Baskerville',serif;color:var(--white);font-size:12.5px;text-decoration:none;padding:0 13px;height:68px;display:flex;align-items:center;position:relative}
.nav a.active{background:rgba(255,255,255,.06)}
.nav a.active::after{content:"";position:absolute;left:50%;bottom:12px;margin-left:-3px;border:3px solid transparent;border-top-color:#fff}
.login{left:995px;top:17px;width:106px;height:34px;background:var(--green);color:#fff;font-family:'Libre Baskerville',serif;font-size:12px;font-weight:700;display:flex;align-items:center;justify-content:center;border-radius:2px}
.socials{left:20px;top:258px;display:flex;flex-direction:column;gap:15px}
.socials span{width:9px;height:9px;border-radius:50%;background:#7e89c4}
.dots{left:1167px;top:258px;display:flex;flex-direction:column;gap:12px}
.dots span{width:10px;height:10px;border:1.5px solid #9aa3d6;border-radius:2px}
.dots span.on{background:var(--green);border-color:var(--green)}
.hero-photo{left:53px;top:68px;width:867px;height:506px;background:linear-gradient(120deg,#d9cdbf,#efe7dc 45%,#a79a8e 75%,#3b3f47)}
.hero-side{left:920px;top:68px;width:226px;height:506px;background:linear-gradient(#f2f1ef,#e9e7e3)}
.hero-text{left:958px;top:232px;font-size:24px;line-height:34px;color:#2b2b2b}
.hero-text b{font-weight:700}
.welcome-accent{left:325px;top:820px;width:109px;height:110px;background:var(--green)}
.welcome-photo{left:161px;top:657px;width:265px;height:264px;background:linear-gradient(135deg,#c9c9c9,#8d8d8d 60%,#3a3a3a)}
h2.title{font-family:'Libre Baskerville',serif;font-weight:700;color:var(--green);font-size:25px}
.welcome-title{left:526px;top:668px}
.welcome-copy{left:526px;top:718px;width:490px;font-size:12px;line-height:19.5px;color:#333}
.welcome-copy p+p{margin-top:24px}
.readmore{font-size:11px;color:var(--green)}
.band-mid{left:0;top:1153px;width:1200px;height:1115px;background:var(--navy)}
.services{left:98px;top:1012px;width:1102px;height:649px;background:var(--white)}
.services-title{left:0;top:1068px;width:1261px;text-align:center}
.dash{color:var(--green);font-weight:400;font-size:18px;margin:0 8px}
.card-big{left:161px;top:1137px;width:433px;height:463px;background:#d7d9de}
.card-big .photo{position:absolute;left:0;top:0;width:433px;height:273px;background:linear-gradient(110deg,#5a5f6a,#9a9ea8 50%,#c9c3bb)}
.card-big .panel{position:absolute;left:4px;top:273px;width:425px;height:186px;background:#fff;padding:20px 22px}
.card-sm{left:616px;width:433px;height:220px;background:#c9b29a}
.card-sm .photo{position:absolute;left:0;top:0;width:217px;height:220px}
.card-sm .panel{position:absolute;left:217px;top:3px;width:212px;height:213px;background:#fff;padding:20px 22px}
.card-title{font-family:'Libre Baskerville',serif;font-weight:700;color:var(--green);font-size:17px;line-height:22px}
.card-copy{font-size:11.5px;line-height:19px;color:#555;margin-top:12px}
.btn{display:inline-flex;align-items:center;justify-content:center;width:119px;height:33px;border:1px solid #cfcfcf;border-radius:2px;font-size:12px;color:#222;margin-top:18px}
.btn.solid{background:var(--green);border-color:var(--green);color:#fff}
.why-title{left:161px;top:1738px;color:#fff;font-size:26px}
.why-list{left:161px;top:1796px;width:510px}
.why-list h4{font-weight:500;color:var(--sky);font-size:13px}
.why-list p{color:#fff;font-size:12px;line-height:18px;margin-top:4px;margin-bottom:22px}
.why-accent{left:930px;top:1960px;width:108px;height:108px;background:var(--green)}
.why-photo{left:751px;top:1743px;width:279px;height:317px;background:linear-gradient(#e5e9ee,#9fb3c8 55%,#2d5ea6)}
.contact{left:0;top:2166px;width:1101px;height:397px;background:#fff}
.contact-title{left:0;top:2232px;width:1200px;text-align:center}
.field{height:37px;border:1px solid var(--line);display:flex;align-items:center;padding-left:12px;gap:8px;font-size:11.5px;color:#777;background:#fff}
.field.tall{align-items:flex-start;padding-top:11px}
.submit{left:552px;top:2462px;width:96px;height:32px;background:var(--navy);color:#fff;font-size:12.5px;font-weight:500;display:flex;align-items:center;justify-content:center;border-radius:2px}
.foot-logo{left:0;top:2632px;width:1200px;text-align:center;color:var(--navy);font-size:34px;font-weight:400}
.suburbs{left:0;top:2682px;width:1200px;text-align:center;font-family:'Libre Baskerville',serif;font-size:11px;color:#777;letter-spacing:.3px}
.suburbs i{font-style:normal;margin:0 15px}
.infobar{left:138px;top:2725px;width:924px;height:77px;background:#fff;box-shadow:0 4px 16px rgba(0,0,0,.05);display:flex;align-items:center;font-size:12.5px;color:#222}
.info{display:flex;align-items:center;gap:12px;position:absolute}
.foot-social{position:absolute;left:764px;top:0;height:77px;border-left:1px solid var(--line);display:flex;align-items:center;gap:20px;padding-left:48px}
.foot-social span{width:11px;height:11px;border-radius:50%;background:#8b8fa3}
.foot-nav{left:0;top:2832px;width:1200px;display:flex;justify-content:center;gap:26px;font-family:'Libre Baskerville',serif;font-size:12.5px}
.foot-nav a{color:#222;text-decoration:none}
.foot-nav a.active{color:var(--navy);text-decoration:underline}
.copyright{left:0;top:2866px;width:1200px;text-align:center;font-size:11.5px;color:#888}
</style>
</head>
<body>
<div class="abs band-top"></div>
<header>
  <div class="abs logo serif">Brevan &amp; Quill</div>
  <nav class="abs nav">
    <a class="active">Home</a><a>Strata</a><a>Rentals</a><a>Insurance and Valuations</a><a>About Us</a><a>Contact Us</a>
  </nav>
  <div class="abs login">Client Login</div>
</header>

<div class="abs socials"><span></span><span></span><span></span><span></span></div>
<div class="abs dots"><span></span><span class="on"></span><span></span><span></span></div>

<section class="hero">
  <div class="abs hero-photo" role="img" aria-label="Agent meeting with a young couple in a bright office"></div>
  <div class="abs hero-side"></div>
  <div class="abs hero-text serif">With<br><b>130 YEARS</b><br>behind us, we<br>have a lot to<br>offer</div>
</section>

<section class="welcome">
  <div class="abs welcome-accent"></div>
  <div class="abs welcome-photo" role="img" aria-label="Black and white photo of two colleagues at a meeting table"></div>
  <h2 class="abs title welcome-title">Welcome to Brevan &amp; Quill</h2>
  <div class="abs welcome-copy">
    <p>The company grew on the strength of its management department and the suc-cessful Auction of residential subdivisions in the developing suburbs of Waverley, Coogee, Randwick and Clovelly.</p>
    <p>In 1912 the company was acquired by Arthur Quill, who continued the growth of the business throughout his stewardship. Intent on a family enterprise he encouraged his sons...</p>
    <p class="readmore" style="margin-top:30px">Read more →</p>
  </div>
</section>

<div class="abs band-mid"></div>
<section>
  <div class="abs services"></div>
  <h2 class="abs title services-title"><span class="dash">--</span>Our Services<span class="dash">--</span></h2>

  <article class="abs card-big">
    <div class="photo" role="img" aria-label="Three colleagues smiling around a laptop"></div>
    <div class="panel">
      <h3 class="card-title">Strata Management</h3>
      <p class="card-copy">Nervous about your property adventure? Don't be. Whether you're getting ready to buy or sell, in the middle of it, or just looking for...</p>
      <span class="btn">Find out more</span>
    </div>
  </article>

  <article class="abs card-sm" style="top:1137px">
    <div class="photo" role="img" aria-label="Small model house with a red roof on a desk" style="background:linear-gradient(135deg,#2d3038,#8a8e96 55%,#e8e4df)"></div>
    <div class="panel">
      <h3 class="card-title">Property<br>Management</h3>
      <p class="card-copy">Large or small, condo or mansion, we can find it and get it for you at the...</p>
      <span class="btn">Find out more</span>
    </div>
  </article>

  <article class="abs card-sm" style="top:1380px;background:#b9bcc2">
    <div class="photo" role="img" aria-label="Two businessmen reviewing documents" style="background:linear-gradient(120deg,#4b4f57,#a8abb2 55%,#dadbdd)"></div>
    <div class="panel">
      <h3 class="card-title">Property Valuation<br>&amp; Brokerage</h3>
      <p class="card-copy">If you have questions about affordability, credit, legal matters, or income, trust...</p>
      <span class="btn solid">Find out more</span>
    </div>
  </article>
</section>

<section>
  <h2 class="abs serif why-title">Why choose us <span style="font-weight:400;font-size:18px">--</span></h2>
  <div class="abs why-list">
    <h4>We are different</h4>
    <p>Established in 1988, we are the longest continuously operating Estate Agent in New South Wales &amp; forth oldest in Australia. We are committed to doing things differently, challenging the norm &amp; are always seeking new &amp; innovative ways...</p>
    <h4>Property Management Expertise</h4>
    <p>Countless Properties &amp; Buildings are cared for by us each &amp; every Year. Our Property Managers are equipt with knowledge, resources &amp; experience allowing us to...</p>
    <h4>Dedicated &amp; qualified Property Managers</h4>
    <p>Our qualified &amp; experienced Property Managers aim to look after your Investment Property as if it was their own. They take responsibility for all Day-to-Day...</p>
    <span class="readmore">Read more →</span>
  </div>
  <div class="abs why-accent"></div>
  <div class="abs why-photo" role="img" aria-label="Smiling businessman in a blue suit with arms crossed"></div>
</section>

<section>
  <div class="abs contact"></div>
  <h2 class="abs title contact-title"><span class="dash">--</span>Get in touch<span class="dash">--</span></h2>
  <div class="abs field" style="left:246px;top:2293px;width:346px">
    <svg width="13" height="13" viewBox="0 0 14 14" fill="none" stroke="#5a68b8" stroke-width="1.2"><circle cx="7" cy="4.5" r="3"/><path d="M1.5 13c0-3 2.5-5 5.5-5s5.5 2 5.5 5"/></svg>Name</div>
  <div class="abs field" style="left:246px;top:2340px;width:346px">
    <svg width="14" height="11" viewBox="0 0 14 11" fill="none" stroke="#5a68b8" stroke-width="1.2"><rect x=".6" y=".6" width="12.8" height="9.8"/><path d="M.6.6 7 6l6.4-5.4"/></svg>Email</div>
  <div class="abs field" style="left:246px;top:2387px;width:346px">
    <svg width="9" height="14" viewBox="0 0 9 14" fill="none" stroke="#5a68b8" stroke-width="1.2"><rect x=".6" y=".6" width="7.8" height="12.8" rx="1.5"/><path d="M3.5 11h2"/></svg>Phone</div>
  <div class="abs field" style="left:607px;top:2293px;width:346px">
    <svg width="11" height="13" viewBox="0 0 11 13" fill="none" stroke="#5a68b8" stroke-width="1.2"><rect x=".6" y=".6" width="9.8" height="11.8"/><path d="M3 3h1M6.5 3h1M3 6h1M6.5 6h1M4 12.4V9.5h3v2.9"/></svg>Service interested
    <svg style="position:absolute;right:12px" width="8" height="5" viewBox="0 0 8 5"><path d="M0 0h8L4 5z" fill="#aaa"/></svg></div>
  <div class="abs field tall" style="left:607px;top:2340px;width:346px;height:84px">
    <svg width="12" height="12" viewBox="0 0 12 12" fill="none" stroke="#5a68b8" stroke-width="1.2"><path d="M.6.6h10.8v7L7.6 11.4H.6z"/></svg>Message</div>
  <div class="abs submit">Submit</div>
</section>

<footer>
  <div class="abs foot-logo serif">Brevan&amp;Quill</div>
  <div class="abs suburbs">COOGEE<i>/</i>WAVERLEY<i>/</i>RANDWICK<i>/</i>CLOVELLY</div>
  <div class="abs infobar">
    <div class="info" style="left:36px">
      <svg width="22" height="28" viewBox="0 0 22 28" fill="none" stroke="var(--navy)" stroke-width="1.5"><path d="M11 27S2 16.5 2 10a9 9 0 0 1 18 0c0 6.5-9 17-9 17z"/><circle cx="11" cy="10" r="3.5"/></svg>
      <span style="line-height:18px">14 - 18 Harlow Lane<br>Randwick NSW 2031</span></div>
    <div class="info" style="left:294px">
      <svg width="19" height="14" viewBox="0 0 19 14" fill="none" stroke="var(--navy)" stroke-width="1.4"><rect x=".7" y=".7" width="17.6" height="12.6"/><path d="M.7.7l8.8 7 8.8-7M.7 13.3l6.5-6M18.3 13.3l-6.5-6"/></svg>admin@brevanquill.com.au</div>
    <div class="info" style="left:545px">
      <svg width="18" height="18" viewBox="0 0 18 18" fill="none" stroke="var(--navy)" stroke-width="1.4"><path d="M4 1.5 6.5 5 5 7c1 2.5 3.5 5 6 6l2-1.5 3.5 2.5-1.5 2.5C9 17 1 9 1.5 3z"/><path d="M11 1.5a5.5 5.5 0 0 1 5.5 5.5M11 4.5A2.5 2.5 0 0 1 13.5 7"/></svg>02 9000 4271</div>
    <div class="foot-social"><span></span><span></span><span></span><span></span></div>
  </div>
  <nav class="abs foot-nav"><a class="active">Home</a><a>Strata</a><a>Rentals</a><a>Insurance and Valuations</a><a>About Us</a><a>Contact Us</a></nav>
  <div class="abs copyright">Copyright © 2021 Brevan&amp;Quill. All Rights Reserved</div>
</footer>
</body>
</html>
```